Business card for a "family office" company

Please provide professional looking business card designs, incorporating the attached logo and below details. Harrowmere Holdings Pty Ltd is a family office / financial investment company. We are looking for a modern, professional and contemporary card design.

Industry/Entity Type

Finance

Contact Information for Business Card

Name: Dean Mollick
Title: Director
Company: Harrowmere Holdings Pty Ltd
Email: harrowdean@quillnet.example
Mobile: 0462 735 418
Address: 4/312 Barnaby Parade, Cottesloe WA 6011, Australia

Requirements
Must have
• All details above and the logo. logo only on back side. incorporate colours of logo
Nice to have
• up to you
Should not have
• ?

```html
<!DOCTYPE html>
<html lang="en">
<head>
<meta charset="utf-8">
<title>Harrowmere Holdings – Business Card</title>
<link href="https://fonts.googleapis.com/css2?family=PT+Sans:wght@400;700&family=Roboto+Slab:wght@700&display=swap" rel="stylesheet">
<style>
  :root {
    --page: #e8e5e0;
    --royal: #2b3a94;
    --navy: #1e2463;
    --ink: #1c1c24;
    --paper: #ffffff;
  }
  * { box-sizing: border-box; margin: 0; padding: 0; }
  html, body {
    width: 1200px; height: 900px; overflow: hidden;
    background: var(--page);
    font-family: "PT Sans", sans-serif;
  }
  .sheet {
    width: 1200px; height: 900px;
    display: flex; flex-direction: column;
    align-items: center; justify-content: center; gap: 48px;
  }
  .card {
    width: 600px; height: 366px;
    position: relative;
    box-shadow: 0 6px 18px rgba(0,0,0,.18);
  }
  /* back side */
  .card--back {
    background: var(--royal);
    display: flex; flex-direction: column; align-items: center; justify-content: center; gap: 22px;
  }
  .brand-mark { width: 26px; height: 26px; background: var(--navy); }
  .brand-name {
    font-family: "PT Sans", sans-serif; font-weight: 400;
    color: var(--navy); text-transform: uppercase;
    font-size: 34px; letter-spacing: 5px; line-height: 1;
  }
  /* front side */
  .card--front { background: var(--paper); padding: 52px 56px 0 58px; }
  .card--front .brand-name { font-size: 27px; letter-spacing: 3.5px; }
  .holder { margin-top: 66px; }
  .holder__name {
    font-family: "Roboto Slab", "Rockwell", "Courier New", serif; font-weight: 700;
    color: var(--royal); font-size: 22px; line-height: 1.1;
    text-transform: uppercase; letter-spacing: .3px;
  }
  .holder__title { color: var(--ink); font-size: 15px; margin-top: 3px; }
  .contact { list-style: none; margin-top: 16px; color: var(--ink); font-size: 15.5px; }
  .contact li { display: flex; align-items: center; gap: 9px; line-height: 1.5; }
  .contact svg { width: 14px; height: 14px; fill: var(--royal); flex: none; }
  .address { margin-top: 18px; color: var(--ink); font-size: 15.5px; line-height: 1.4; font-style: normal; }
</style>
</head>
<body>
<main class="sheet">
  <section class="card card--back" aria-label="Card back">
    <span class="brand-mark"></span>
    <span class="brand-name">Harrowmere Holdings</span>
  </section>

  <section class="card card--front" aria-label="Card front">
    <div class="brand-name">Harrowmere Holdings</div>
    <div class="holder">
      <h1 class="holder__name">Dean Mollick</h1>
      <p class="holder__title">Director</p>
    </div>
    <ul class="contact">
      <li>
        <svg viewBox="0 0 24 24" aria-hidden="true"><path d="M6.6 10.8a15.1 15.1 0 0 0 6.6 6.6l2.2-2.2c.3-.3.7-.4 1-.2 1.1.4 2.3.6 3.6.6.6 0 1 .4 1 1V20c0 .6-.4 1-1 1A17 17 0 0 1 3 4c0-.6.4-1 1-1h3.5c.6 0 1 .4 1 1 0 1.3.2 2.5.6 3.6.1.3 0 .7-.2 1z"/></svg>
        0462 735 418
      </li>
      <li>
        <svg viewBox="0 0 24 24" aria-hidden="true"><path d="M2 5h20v14H2V5zm2 2v.4l8 5.2 8-5.2V7H4z"/></svg>
        harrowdean@quillnet.example
      </li>
    </ul>
    <address class="address">4/312 Barnaby Parade,<br>Cottesloe WA 6011, Australia</address>
  </section>
</main>
</body>
</html>
```